Business card design needed

Family General Practitioner/ Family Physician.
Logo is the logo of the Imperial Guild of Community Clinicians Oceania
http://pkvtm.lorimar.example/PictureGallery/logos/pages/IGCCO%20logo_jpg.htm

Reason: Just a bit more time to make changes and the weekend for me to look at things closely and to choose. Thanks, Ulan

Thanks for all the submissions. So many of them are really works of art. Not one of them are not good. The ones that I am eliminating are the ones that I think are not suitable for me personally only, and because if I don't, it makes it very difficult to decide as many of you are also sending me slight variations of a card. I have just decided to choose a second place card too. Can't thank you all enough. Good luck, Ulan. P.S - Working today till 10 pm as the card says :-), so probably won't be able to give a feedback till late Saturday night or Sunday morning here in Sydney, Australia. 

Reason: Just added a second place to the budget and realised that Australia is ahead of the rest of the world in the time zone (only :-) - don't want to offend anyone or start a debate!! ) , so Monday deadline will mean it will be a weekend for the rest of the world. Just wanted to give everyone more time to submit their best, especially since I will be picking a second card too. Can't thank everyone enough for the submissions. P.S - Not keen on photos on the card.

Business

Contact Information for Business Card

Dr. Ulan Pereira M.B.B.S., F.I.G.C.C.O
Family General Practitioner
Address, timings, phone and fax number on the back.

Requirements
Must have
• Timings
Mon 7 am - 7 pm
Tues 7 am - 12 pm
Wed 7 am - 10 pm
Thurs 7 am - 12 pm
Fri 7 am - 8 pm
Sat 8 am - 10 pm
Sun - Off

```html
<!DOCTYPE html>
<html lang="en">
<head>
<meta charset="utf-8">
<title>Dr. Ulan Pereira – Business Card</title>
<link rel="stylesheet" href="https://fonts.googleapis.com/css2?family=Open+Sans:wght@400;700;800&family=Tinos:wght@400;700&display=swap">
<style>
  :root {
    --page: #ece8e3;
    --blue-deep: #2f55a0;
    --blue-light: #46bad9;
    --grey-light: #e6e6e6;
    --grey-mid: #b9b9b9;
    --ink: #1a1a1a;
    --white: #ffffff;
    --red: #ef4b3a;
    --purple: #8a2a7a;
    --label: #ffffff;
    --label-bg: #5a3a22;
    --gold: #c8a24a;
  }
  * { box-sizing: border-box; margin: 0; padding: 0; }
  html, body { width: 1200px; height: 739px; overflow: hidden; }
  body { background: var(--page); position: relative; font-family: "Open Sans", sans-serif; }

  .card { position: absolute; width: 525px; height: 300px; overflow: hidden; box-shadow: 0 2px 6px rgba(0,0,0,.25); }
  .card-bg { position: absolute; inset: 0; }

  /* front */
  .card--front { left: 40px; top: 28px; }
  .front-name { position: absolute; top: 30px; left: 0; width: 525px; text-align: center; font-family: "Tinos", serif; color: var(--white); font-size: 42px; font-variant: small-caps; letter-spacing: 2px; line-height: 1; }
  .front-creds { position: absolute; top: 83px; left: 0; width: 525px; text-align: center; font-family: "Tinos", serif; color: var(--white); font-size: 11px; letter-spacing: 1px; }
  .front-role { position: absolute; top: 121px; left: 0; width: 525px; text-align: center; font-family: "Tinos", serif; color: var(--white); font-size: 19px; letter-spacing: 2px; }
  .front-tagline { position: absolute; top: 265px; left: 113px; font-family: "Tinos", serif; font-weight: 700; font-size: 22px; color: var(--ink); }
  .front-mark { position: absolute; left: 418px; top: 232px; display: flex; align-items: center; gap: 5px; font-weight: 700; font-size: 17px; color: var(--blue-deep); }
  .front-mark::before { content: ""; width: 14px; height: 14px; border-radius: 50%; background: var(--blue-deep); }

  /* back */
  .card--opt1 { left: 615px; top: 27px; }
  .card--opt2 { left: 47px; top: 368px; }
  .card--opt3 { left: 611px; top: 376px; }
  .hours-title { position: absolute; top: 16px; left: 38px; color: var(--white); font-size: 19px; }
  .card--opt2 .hours-title { left: 50px; top: 6px; font-size: 20px; letter-spacing: 1px; }
  .hours { position: absolute; left: 38px; top: 46px; color: var(--white); list-style: none; font-size: 15px; line-height: 23px; }
  .card--opt2 .hours { left: 31px; top: 42px; }
  .hours--caps { font-weight: 800; text-transform: uppercase; font-size: 15px; }
  .hours b { font-weight: 700; }
  .card--opt2 .day { display: inline-block; width: 109px; }
  .watermark { position: absolute; right: 48px; top: 80px; font-weight: 700; font-size: 46px; color: rgba(255,255,255,.08); }
  .back-address { position: absolute; left: 0; width: 525px; top: 229px; text-align: center; font-family: "Tinos", serif; font-size: 14.5px; line-height: 17px; color: var(--ink); }
  .back-phone { position: absolute; left: 0; width: 525px; top: 274px; text-align: center; font-family: "Tinos", serif; font-size: 14.5px; color: var(--ink); }
  .card--opt2 .back-address { top: 229px; }
  .back-phone .sep { display: inline-block; width: 1px; height: 16px; background: var(--ink); margin: 0 6px; vertical-align: -3px; }

  .option-label { position: absolute; font-weight: 800; font-size: 20px; color: var(--label); text-shadow: 0 0 3px var(--label-bg), 0 0 6px var(--label-bg); }
</style>
</head>
<body>

<svg width="0" height="0" style="position:absolute">
  <defs>
    <linearGradient id="blueGrad" x1="0" y1="0" x2="1" y2="0">
      <stop offset="0" stop-color="#2f55a0"/>
      <stop offset="1" stop-color="#46bad9"/>
    </linearGradient>
    <linearGradient id="greyGrad" x1="0" y1="0" x2="1" y2="0">
      <stop offset="0" stop-color="#cfcfcf"/>
      <stop offset=".5" stop-color="#efefef"/>
      <stop offset="1" stop-color="#c4c4c4"/>
    </linearGradient>
  </defs>
</svg>

<!-- Front -->
<div class="card card--front">
  <svg class="card-bg" viewBox="0 0 525 300" width="525" height="300">
    <rect width="525" height="300" fill="url(#blueGrad)"/>
    <path d="M0 262 C160 262 300 200 525 170 L525 300 L0 300 Z" fill="url(#greyGrad)"/>
    <path d="M0 250 C120 240 210 220 230 215 C180 232 90 252 0 258 Z" fill="#e0503e"/>
    <path d="M0 265 C180 262 330 180 525 160 L525 166 C330 190 180 270 0 272 Z" fill="var(--purple)"/>
    <path d="M0 258 C170 252 320 165 525 150 L525 158 C320 175 170 262 0 264 Z" fill="var(--red)"/>
    <path d="M370 190 C420 178 470 172 525 172 L525 177 C470 178 420 184 370 190 Z" fill="var(--red)"/>
  </svg>
  <div class="front-name">Dr. Ulan Pereira</div>
  <div class="front-creds">M.B.B.S., F.I.G.C.C.O</div>
  <div class="front-role">Family General Practitioner</div>
  <div class="front-mark">IGCCO</div>
  <div class="front-tagline">Caring about your health</div>
</div>

<!-- Option 1 -->
<div class="card card--opt1">
  <svg class="card-bg" viewBox="0 0 525 300" width="525" height="300">
    <rect width="525" height="300" fill="url(#greyGrad)"/>
    <rect width="525" height="220" fill="url(#blueGrad)"/>
    <rect y="220" width="525" height="2" fill="var(--gold)"/>
  </svg>
  <div class="watermark">IGCCO</div>
  <div class="hours-title">Working Hours</div>
  <ul class="hours hours--caps">
    <li>Monday&nbsp;&nbsp; 7 AM &nbsp;- 7 PM</li>
    <li>Tuesday&nbsp; 7 AM - 12 PM</li>
    <li>Wednesday&nbsp; 7 AM - 10 PM</li>
    <li>Thursday&nbsp; 7 AM - 12 PM</li>
    <li>Friday&nbsp;&nbsp;&nbsp; 7 AM &nbsp;- 8 PM</li>
    <li>Saturday&nbsp; 8 AM - 10 PM</li>
    <li>Sunday - Off</li>
  </ul>
  <p class="back-address">Lower Level, Juniper Arcade, Wattle Grove Shopping Centre<br>Brennan Hill, NSW 2190</p>
  <p class="back-phone">P: 02 9471 3600<span class="sep"></span>F: 02 9471 3655</p>
</div>
<div class="option-label" style="left:823px;top:339px">Option# 1</div>

<!-- Option 2 -->
<div class="card card--opt2">
  <svg class="card-bg" viewBox="0 0 525 300" width="525" height="300">
    <rect width="525" height="300" fill="url(#greyGrad)"/>
    <rect width="525" height="220" fill="url(#blueGrad)"/>
    <rect y="220" width="525" height="2" fill="var(--gold)"/>
  </svg>
  <div class="watermark">IGCCO</div>
  <div class="hours-title">Working Hours</div>
  <ul class="hours">
    <li><span class="day">Monday</span><b>7 AM &nbsp;- 7 PM</b></li>
    <li><span class="day">Tuesday</span><b>7 AM - 12 PM</b></li>
    <li><span class="day">Wednesday</span><b>7 AM - 10 PM</b></li>
    <li><span class="day">Thursday</span><b>7 AM - 12 PM</b></li>
    <li><span class="day">Friday</span><b>7 AM &nbsp;- 8 PM</b></li>
    <li><span class="day">Saturday</span><b>8 AM - 10 PM</b></li>
    <li><span class="day">Sunday</span><b>OFF</b></li>
  </ul>
  <p class="back-address">Lower Level, Juniper Arcade, Wattle Grove Shopping Centre<br>Brennan Hill, NSW 2190</p>
  <p class="back-phone">P: 02 9471 3600<span class="sep"></span>F: 02 9471 3655</p>
</div>
<div class="option-label" style="left:255px;top:680px">Option# 2</div>

<!-- Option 3 -->
<div class="card card--opt3">
  <svg class="card-bg" viewBox="0 0 525 300" width="525" height="300">
    <rect width="525" height="300" fill="url(#greyGrad)"/>
    <rect width="525" height="220" fill="url(#blueGrad)"/>
    <rect y="220" width="525" height="2" fill="var(--gold)"/>
  </svg>
  <div class="watermark">IGCCO</div>
  <div class="hours-title">Working Hours</div>
  <ul class="hours">
    <li>Monday&nbsp; <b>7 AM &nbsp;- 7 PM</b></li>
    <li>Tuesday&nbsp; <b>7 AM - 12 PM</b></li>
    <li>Wednesday&nbsp; <b>7 AM - 10 PM</b></li>
    <li>Thursday&nbsp; <b>7 AM - 12 PM</b></li>
    <li>Friday&nbsp;&nbsp;&nbsp; <b>7 AM &nbsp;- 8 PM</b></li>
    <li>Saturday&nbsp; <b>8 AM - 10 PM</b></li>
    <li>Sunday - <b>OFF</b></li>
  </ul>
  <p class="back-address">Lower Level, Juniper Arcade, Wattle Grove Shopping Centre<br>Brennan Hill, NSW 2190</p>
  <p class="back-phone">P: 02 9471 3600<span class="sep"></span>F: 02 9471 3655</p>
</div>
<div class="option-label" style="left:820px;top:687px">Option# 3</div>

</body>
</html>
```